Brevora Ad Image Design Competition

We're seeking creative designers to develop a series of engaging Brevora advertisements for Moltcraft with original art work.

The goal is to create scroll-stopping ads that capture attention through humor, nostalgia, and compelling storytelling while maintaining professional appeal.

Creative Brief:
Please read the "Core Messages to Convey"
https://pages.quillbarn.net/sheet/p/7kRtw2QmLv9xNcBe4HjYa63-s08ZueTFd_q51hnWpZ3/view?tab=t.0#heading=h.4mrwtzcja2k

Target Market(s)

Busy executives focusing on making their company more efficient

Requirements
Must have
• An image ( not copy) that speaks to one of our "Core Messages to Convey"

```html
<!DOCTYPE html>
<html lang="en">
<head>
<meta charset="utf-8">
<title>Moltcraft – Accelerate Your Value Creation Journey</title>
<link href="https://fonts.googleapis.com/css2?family=Bebas+Neue&family=League+Spartan:wght@600;700;800&display=swap" rel="stylesheet">
<style>
  :root {
    --stage: #6a6a6a;
    --paper-top: #ece8ef;
    --paper-bottom: #c8ccd6;
    --blush: #e7c3d8;
    --ink-grey: #4e4e52;
    --ink-plum: #4b0d3a;
    --ink-red: #b3121c;
    --ink-red-dark: #8a0c14;
    --night-red: #6d0418;
    --night-violet: #7b2fc9;
    --bar-face: #dcdce0;
    --bar-side: #a9a9ae;
    --bar-top: #efd9e2;
  }
  * { margin: 0; padding: 0; box-sizing: border-box; }
  html, body { width: 1200px; height: 943px; overflow: hidden; background: var(--stage); }
  .ad {
    position: absolute; left: 150px; top: 22px; width: 900px; height: 900px; overflow: hidden;
    background:
      radial-gradient(ellipse 55% 45% at 78% 42%, var(--blush) 0%, rgba(231,195,216,0) 70%),
      linear-gradient(180deg, var(--paper-top) 0%, #dcdbe3 50%, var(--paper-bottom) 100%);
  }
  .ad-art { position: absolute; inset: 0; width: 900px; height: 900px; }
  .headline { position: absolute; left: 0; top: 0; font-family: "League Spartan", sans-serif; }
  .kicker {
    position: absolute; left: 66px; top: 190px; font-size: 48px; font-weight: 800;
    line-height: 46px; letter-spacing: -0.5px; color: var(--ink-grey); text-transform: uppercase;
  }
  .value {
    position: absolute; left: 64px; top: 284px; font-size: 77px; font-weight: 800;
    line-height: 72px; letter-spacing: -1px; color: var(--ink-plum); white-space: nowrap; text-transform: uppercase;
  }
  .journey {
    position: absolute; left: 58px; top: 420px; font-family: "Bebas Neue", sans-serif;
    font-size: 176px; line-height: 1; color: var(--ink-red); letter-spacing: 0;
    background: linear-gradient(180deg, var(--ink-red) 0%, var(--ink-red-dark) 100%);
    -webkit-background-clip: text; background-clip: text; -webkit-text-fill-color: transparent;
  }
  .brand { position: absolute; left: 66px; top: 780px; display: flex; align-items: center; gap: 14px; }
  .brand-dot { width: 28px; height: 28px; border-radius: 50%; background: var(--ink-plum); }
  .brand-name {
    font-family: "League Spartan", sans-serif; font-weight: 600; font-size: 46px;
    line-height: 1; color: var(--ink-plum);
  }
</style>
</head>
<body>
  <main class="ad">
    <svg class="ad-art" viewBox="0 0 1194 1192" xmlns="http://www.w3.org/2000/svg">
      <defs>
        <linearGradient id="night" x1="0" y1="0" x2="1" y2="0.4">
          <stop offset="0" stop-color="var(--night-red)"/>
          <stop offset="0.6" stop-color="var(--night-violet)"/>
          <stop offset="1" stop-color="var(--night-red)"/>
        </linearGradient>
        <radialGradient id="clock" cx="0.55" cy="0.45" r="0.6">
          <stop offset="0" stop-color="#f7f1f5"/>
          <stop offset="0.7" stop-color="#e6cddb"/>
          <stop offset="1" stop-color="#d9b4c9" stop-opacity="0"/>
        </radialGradient>
        <linearGradient id="arrow" x1="0" y1="1" x2="1" y2="0">
          <stop offset="0" stop-color="#9a0c14"/>
          <stop offset="1" stop-color="#e01a24"/>
        </linearGradient>
      </defs>

      <path class="clock-backdrop" role="img" aria-label="Dark red and violet backdrop of glowing clock faces"
            fill="url(#night)"
            d="M377 0 H1194 V578 L1157 458 L1127 378 L1087 298 L677 118 L587 108 L537 78 L447 33 Z"/>
      <ellipse class="shattering-clock" role="img" aria-label="Wall clock shattering into glass shards and gears"
               cx="880" cy="250" rx="240" ry="230" fill="url(#clock)"/>

      <g class="bar-chart">
        <g class="bar"><polygon fill="var(--bar-face)" points="474,853 492,853 492,915 474,908"/><polygon fill="var(--bar-side)" points="492,853 509,853 509,921 492,915"/></g>
        <g class="bar"><polygon fill="var(--bar-face)" points="507,843 527,843 527,936 507,928"/><polygon fill="var(--bar-side)" points="527,843 545,843 545,943 527,936"/></g>
        <g class="bar"><polygon fill="var(--bar-face)" points="545,843 567,843 567,962 545,953"/><polygon fill="var(--bar-side)" points="567,843 587,843 587,970 567,962"/></g>
        <g class="bar"><polygon fill="var(--bar-face)" points="585,833 608,833 608,988 585,978"/><polygon fill="var(--bar-side)" points="608,833 629,833 629,997 608,988"/></g>
        <g class="bar"><polygon fill="var(--bar-face)" points="627,818 654,818 654,1019 627,1008"/><polygon fill="var(--bar-side)" points="654,818 677,818 677,1029 654,1019"/></g>
        <g class="bar"><polygon fill="var(--bar-face)" points="675,786 705,786 705,1051 675,1038"/><polygon fill="var(--bar-side)" points="705,786 730,786 730,1062 705,1051"/></g>
        <g class="bar"><polygon fill="var(--bar-face)" points="730,743 762,743 762,1087 730,1073"/><polygon fill="var(--bar-side)" points="762,743 789,743 789,1099 762,1087"/></g>
        <g class="bar"><polygon fill="var(--bar-face)" points="789,638 825,638 825,1124 789,1108"/><polygon fill="var(--bar-side)" points="825,638 855,638 855,1138 825,1124"/></g>
        <g class="bar"><polygon fill="var(--bar-face)" points="857,518 912,518 912,1170 857,1148"/><polygon fill="var(--bar-side)" points="912,518 967,518 967,1150 912,1170"/></g>
        <g class="bar-tops" fill="var(--bar-top)">
          <rect x="474" y="850" width="35" height="5"/><rect x="507" y="840" width="38" height="5"/>
          <rect x="545" y="840" width="42" height="5"/><rect x="585" y="830" width="44" height="5"/>
          <rect x="627" y="815" width="50" height="5"/><rect x="675" y="783" width="55" height="5"/>
          <rect x="730" y="740" width="59" height="5"/><rect x="789" y="635" width="66" height="5"/>
          <rect x="857" y="515" width="110" height="5"/>
        </g>
      </g>

      <g class="growth-arrow">
        <path d="M492 818 C640 808 770 730 800 500" fill="none" stroke="url(#arrow)" stroke-width="22" stroke-linecap="round"/>
        <polygon fill="url(#arrow)" points="712,508 867,508 837,303"/>
      </g>
    </svg>

    <h1 class="headline">
      <span class="kicker">Accelerate<br>Your</span>
      <span class="value">Value<br>Creation</span>
      <span class="journey">JOURNEY</span>
    </h1>

    <div class="brand">
      <span class="brand-dot"></span>
      <span class="brand-name">Moltcraft</span>
    </div>
  </main>
</body>
</html>
```